iron deficiency anemia - educational reference paper

looking for an educational paper/poster 8x11 or no larger than 11x14 that lists the most common foods with pictures and limited words a super rough outline attached - I wrote the words of the pictures (but would like to have the actual pictures of these items) I would like in roughly the same order
for the pictures for fatigue, headache....can be drawings or cartoons
double sided or single sided (which ever fits) see attached for categories (3 of them)

Target Market(s)

educational for people with limited education - thus not much wording

Requirements
Must have
• pictures, simple design

```html
<!DOCTYPE html>
<html lang="en">
<head>
<meta charset="utf-8">
<title>Iron Deficiency Anemia</title>
<link rel="stylesheet" href="https://fonts.googleapis.com/css2?family=Open+Sans:wght@700;800&family=PT+Sans:wght@400;700&display=swap">
<style>
  :root{
    --page:#ffffff;
    --sky:#7fb2f7;
    --sky-light:#a9cbf8;
    --stripe:#c9ddf9;
    --panel:#f7f5f5;
    --food-panel:#80b1f2;
    --navy:#0d1e3a;
    --frame:#0f1a2e;
    --tile-border:#7fb2f7;
  }
  *{margin:0;padding:0;box-sizing:border-box}
  html,body{width:927px;height:1200px;overflow:hidden;background:var(--page)}
  .stage{position:relative;width:860px;height:1100px;transform:scale(1.0779,1.0909);transform-origin:0 0}
  .poster{position:absolute;left:60px;top:70px;width:748px;height:952px;background:var(--sky);border:1px solid #3a4a66;overflow:hidden}
  .stripe{position:absolute;top:0;bottom:0;background:var(--stripe)}
  .stripe.s1{left:40px;width:5px}
  .stripe.s2{left:50px;width:14px;background:var(--sky-light)}
  .title{position:absolute;left:0;right:0;top:22px;text-align:center;font-family:"Open Sans",sans-serif;font-weight:800;font-size:50px;letter-spacing:1.5px;color:var(--navy)}
  .panel{position:absolute;left:10px;top:98px;width:738px;height:504px;background:var(--panel);border-radius:160px 0 0 130px}
  .heading{font-family:"Open Sans",sans-serif;font-weight:800;color:var(--navy);line-height:1.05}
  .symptoms-title{position:absolute;left:40px;top:130px;width:260px;text-align:center;font-size:37px}
  .symptom{position:absolute;width:130px;text-align:center}
  .symptom .photo{width:130px;height:73px;border:2px solid var(--tile-border)}
  .symptom .label{font-family:"PT Sans",sans-serif;font-weight:700;font-size:16px;color:var(--navy);margin-top:4px}
  .food{position:absolute;left:308px;top:118px;width:432px;height:462px;background:var(--food-panel);border:2px solid #a9c9f5}
  .food-title{position:absolute;left:80px;right:0;top:4px;text-align:center;font-size:27px}
  .food-sub{position:absolute;left:80px;right:0;top:60px;text-align:center;font-size:19px}
  .food-col{position:absolute;left:6px;top:24px;width:80px}
  .food-col .tile{width:78px;height:48px;margin-bottom:4.5px}
  .food-row{position:absolute;left:6px;top:396px;display:flex;gap:4px}
  .food-row .tile{width:78px;height:50px}
  .food-list{position:absolute;top:88px;list-style:none;font-family:"PT Sans",sans-serif;font-size:14px;line-height:16.7px;color:var(--navy)}
  .food-list.c1{left:102px}.food-list.c2{left:219px}.food-list.c3{left:335px}
  .sign{position:absolute;border:5px solid var(--frame);display:flex;gap:4px;background:var(--frame)}
  .sign .photo{flex:1}
  .caption{position:absolute;font-family:"Open Sans",sans-serif;font-weight:700;font-size:14px;color:var(--navy)}
  .signs-title{position:absolute;left:13px;top:800px;font-size:43px;line-height:1.03}
</style>
</head>
<body>
<div class="stage">
  <div class="poster">
    <div class="stripe s1"></div>
    <div class="stripe s2"></div>
    <h1 class="title">IRON DEFICIENCY ANEMIA</h1>

    <div class="panel"></div>
    <h2 class="heading symptoms-title">SYMPTOMS<br>OF<br>ANEMIA</h2>

    <div class="symptom" style="left:23px;top:252px"><div class="photo" role="img" aria-label="Person lying in bed, tired" style="background:linear-gradient(#b9c3d4,#e8e6ea)"></div><div class="label">Fatigue</div></div>
    <div class="symptom" style="left:161px;top:252px"><div class="photo" role="img" aria-label="Person holding head with headache" style="background:linear-gradient(#e3e2e0,#c8bcb0)"></div><div class="label">Headache</div></div>
    <div class="symptom" style="left:23px;top:374px"><div class="photo" role="img" aria-label="Dizzy person holding head" style="background:linear-gradient(90deg,#d9d9d9,#a9a39c,#e4e4e4)"></div><div class="label">Dizziness</div></div>
    <div class="symptom" style="left:161px;top:374px"><div class="photo" role="img" aria-label="Blurred night lights" style="background:linear-gradient(135deg,#0f1e30,#324a66,#1a2533)"></div><div class="label">Blurry Vision</div></div>
    <div class="symptom" style="left:93px;top:493px"><div class="photo" role="img" aria-label="Person holding weak arm" style="background:linear-gradient(#ddd9d6,#c7b9ad)"></div><div class="label">Muscle Weakness</div></div>

    <section class="food">
      <h2 class="heading food-title">COMMON FOODS<br>IN YOUR COMMUNITY</h2>
      <p class="heading food-sub">( IRON RICH FOODS )</p>
      <div class="food-col">
        <div class="tile" role="img" aria-label="Cow in a field" style="background:linear-gradient(#cfe0c0,#6f9a4a)"></div>
        <div class="tile" role="img" aria-label="Mushrooms" style="background:linear-gradient(#8a6a50,#3a2a20)"></div>
        <div class="tile" role="img" aria-label="Soybeans" style="background:linear-gradient(#e0c070,#8fb050)"></div>
        <div class="tile" role="img" aria-label="Peanuts in a bowl" style="background:linear-gradient(#f2f2f2,#d9b070)"></div>
        <div class="tile" role="img" aria-label="Shrimp" style="background:linear-gradient(#b07a5a,#6a4a3a)"></div>
        <div class="tile" role="img" aria-label="Carrots" style="background:linear-gradient(#f0f0f0,#e07830)"></div>
        <div class="tile" role="img" aria-label="Pig" style="background:linear-gradient(#6a8a50,#d8a898)"></div>
      </div>
      <div class="food-row">
        <div class="tile" role="img" aria-label="Broccoli" style="background:linear-gradient(#f4f4f4,#4f8a3a)"></div>
        <div class="tile" role="img" aria-label="Sardines" style="background:linear-gradient(#6a7a8a,#c8ccd0)"></div>
        <div class="tile" role="img" aria-label="Sesame seeds on a spoon" style="background:linear-gradient(#e8d8b8,#b08850)"></div>
        <div class="tile" role="img" aria-label="Tomatoes" style="background:linear-gradient(#e03020,#a01810)"></div>
        <div class="tile" role="img" aria-label="Turkeys" style="background:linear-gradient(#d8d8d0,#5a5048)"></div>
      </div>
      <ul class="food-list c1"><li>Sheep / Lamb</li><li>Goose</li><li>Whale</li><li>Winged Bean</li><li>Rice Bran</li><li>White&nbsp; Bean</li><li>Pig / Pork</li><li>Kidney Bean</li><li>Cowpea</li><li>Black Bean</li><li>Mung Bean</li><li>Natto</li><li>Teff</li><li>Amaranth</li><li>Chili / Pink Bean</li><li>Lentil</li><li>Yellow Bean</li><li>Pumpkin Seed</li></ul>
      <ul class="food-list c2"><li>Fava Bean</li><li>Sesame Seed</li><li>Aduzki Bean</li><li>Cranberry Bean</li><li>Masa</li><li>Split Peas</li><li>Cuttlefish</li><li>Bear</li><li>Sunflower Seed</li><li>Bagal</li><li>Sardines</li><li>Chickpeas</li><li>Shrimp</li><li>Spinach</li><li>Beet</li><li>Brussel Sprouts</li><li>Collard Greens</li><li>Lima Bean</li></ul>
      <ul class="food-list c3"><li>Turkey</li><li>Blackberry</li><li>Broccoli</li><li>Carrot</li><li>Cauliflower</li><li>Halibut</li><li>Tomato</li><li>Squab</li><li>Turkey</li><li>Pigeon Pea</li><li>Tortilla</li><li>Potato</li><li>Nuts</li><li>Chicken</li><li>Duck</li><li>Egg</li><li>Mushroom</li></ul>
    </section>

    <div class="sign" style="left:165px;top:622px;width:331px;height:135px">
      <div class="photo" role="img" aria-label="Normal eye with red inner eyelid" style="background:linear-gradient(#e8cfc8,#d0606a)"></div>
      <div class="photo" role="img" aria-label="Anemic eye with pale inner eyelid" style="background:linear-gradient(#d8c8c0,#f0c8b8)"></div>
    </div>
    <span class="caption" style="left:191px;top:759px">NORMAL</span>
    <span class="caption" style="left:396px;top:759px">ANEMIC</span>

    <div class="sign" style="left:536px;top:624px;width:176px;height:133px;background:#1a2538">
      <div class="photo" role="img" aria-label="Normal pink palm and pale anemic palm" style="background:linear-gradient(90deg,#c89088,#d8c0b8 50%,#e0cac0)"></div>
    </div>
    <span class="caption" style="left:536px;top:759px">NORMAL</span>
    <span class="caption" style="left:649px;top:759px">ANEMIC</span>

    <h2 class="heading signs-title">SIGNS<br>OF<br>ANEMIA</h2>

    <div class="sign" style="left:268px;top:792px;width:191px;height:132px">
      <div class="photo" role="img" aria-label="Pale anemic fingernails" style="background:linear-gradient(#f2eeee,#c8a8b0)"></div>
    </div>
    <span class="caption" style="left:328px;top:928px">ANEMIC</span>

    <div class="sign" style="left:501px;top:792px;width:224px;height:132px">
      <div class="photo" role="img" aria-label="Normal pink tongue" style="background:linear-gradient(#b89078,#e0a0a0)"></div>
      <div class="photo" role="img" aria-label="Anemic pale smooth tongue" style="background:linear-gradient(#a88870,#e8c8c0)"></div>
    </div>
    <span class="caption" style="left:504px;top:928px">NORMAL</span>
    <span class="caption" style="left:656px;top:928px">ANEMIC</span>
  </div>
</div>
</body>
</html>
```